Design a Wordpress based website for selling Tiny homes

Needs to be Wordpress based. 3-4 pages of content. I will be supplying most of the pictures, the other images can be stock.

Target Market(s)

Young couples, students, mum/dad, property developers

Industry/Entity Type

Home Builder

Logo Text

Tiny Haven Homes

Coding

Coded - Design and coding required

Number of Pages Required

4 page

Colors

Designer to choose colors to be used in the design.

Requirements
Must have
• Top menu must have (Home, Models, Tiny Homes, Order). See "Capture.JPEG" and link for text/script to copy - https://example-tinyhaven.net/site-1
• Logo should be based on the text "Tiny Haven Homes"
Nice to have
• Similar positioning of text and layout to what the "Capture.jpeg" has OR better.

```html
<!DOCTYPE html>
<html lang="en">
<head>
<meta charset="utf-8">
<title>Tiny Haven Homes</title>
<link href="https://fonts.googleapis.com/css2?family=Merriweather:ital,wght@0,400;0,700;1,400;1,700&family=Montserrat:wght@400;500;600;700&display=swap" rel="stylesheet">
<style>
:root{
  --red:#8e0d13;
  --red-bright:#c4161c;
  --navy:#1f2d50;
  --navy-dark:#17223d;
  --ink:#2b2b2b;
  --muted:#6b6b6b;
  --line:#e2e2e2;
  --pale:#f3f3f3;
  --white:#fff;
  --card:#4a4a4a;
}
*{box-sizing:border-box;margin:0;padding:0}
html,body{width:1200px;height:4296px;overflow:hidden}
body{font-family:"Montserrat",sans-serif;color:var(--ink);background:var(--white);position:relative}
section,header,footer{position:absolute;left:0;width:1200px}

/* header */
.site-header{top:0;height:103px;background:var(--white);box-shadow:0 2px 6px rgba(0,0,0,.08);z-index:3}
.brand{position:absolute;left:180px;top:22px;display:flex;align-items:center;gap:10px}
.brand-mark{width:22px;height:22px;background:var(--red)}
.brand-name{font-weight:700;font-size:20px;color:var(--red);text-transform:uppercase;line-height:1.05;width:120px}
.account-tab{position:absolute;right:80px;top:0;width:236px;height:28px;background:var(--red);display:flex;justify-content:center;align-items:center;gap:26px;font-size:10px;color:var(--white);letter-spacing:.5px}
.account-tab span{display:flex;align-items:center;gap:6px}
.main-nav{position:absolute;left:584px;top:54px;display:flex;gap:36px;font-size:12px;font-weight:500;text-transform:uppercase}
.main-nav a{color:var(--ink);text-decoration:none;padding-bottom:8px}
.main-nav a.active{border-bottom:3px solid var(--red)}

/* hero */
.hero{top:103px;height:613px;background:linear-gradient(160deg,#6f8a5a 0%,#4a6a44 28%,#8a5a44 45%,#5c6f82 62%,#3c4a3c 100%);overflow:hidden}
.hero::after{content:"";position:absolute;inset:0;background:rgba(0,0,0,.32)}
.hero-inner{position:absolute;left:0;right:0;top:230px;text-align:center;color:var(--white);z-index:1}
.hero h1{font-family:"Merriweather",serif;font-weight:400;font-size:48px;letter-spacing:.5px}
.hero p{width:760px;margin:30px auto 0;font-size:15px;line-height:1.7}
.btn{display:inline-block;background:var(--red);color:var(--white);font-size:12px;font-weight:600;text-transform:uppercase;padding:11px 30px;letter-spacing:.5px}
.hero .btn{margin-top:36px;padding:12px 44px}
.hero-arrow{position:absolute;top:290px;width:50px;height:50px;border-radius:50%;background:rgba(255,255,255,.85);z-index:1;display:flex;align-items:center;justify-content:center}
.hero-arrow.prev{left:62px}.hero-arrow.next{right:62px}

/* highlights */
.highlights{top:716px;height:472px;background:linear-gradient(180deg,#d8d4cf,#c9c4bf)}
.offer-card{position:absolute;left:195px;top:30px;width:392px;height:418px;background:var(--card);color:var(--white);text-align:center;padding:22px 24px}
.offer-card h2{font-family:"Merriweather",serif;font-weight:400;font-size:18px;line-height:1.35}
.offer-card .sleeps{color:#9fb7d8;font-size:12px;margin-top:6px;letter-spacing:1px}
.offer-photo{width:286px;height:150px;margin:14px auto 0;background:linear-gradient(160deg,#9fc24c,#6f9a2a 60%,#4a6a2a)}
.offer-card .note{font-size:12px;margin-top:10px}
.offer-card .price{font-family:"Merriweather",serif;font-size:24px;margin-top:20px}
.offer-card .tc{font-size:10px;margin-top:2px}
.offer-card .btn{margin-top:14px;padding:9px 42px}
.likes{position:absolute;left:665px;top:36px;width:420px}
.likes h3{font-size:17px;font-weight:400;line-height:1.5}
.likes h3 b{font-weight:700;text-transform:uppercase}
.likes ul{list-style:none;margin-top:20px}
.likes li{display:flex;align-items:center;gap:14px;font-size:13px;height:38px}
.plus{width:20px;height:20px;border-radius:50%;border:2px solid var(--red-bright);color:var(--red-bright);font-size:14px;line-height:15px;text-align:center;font-weight:700}

/* band */
.question-band{top:1188px;height:182px;background:var(--red);color:var(--white);text-align:center}
.question-band p{width:880px;margin:36px auto 0;font-family:"Merriweather",serif;font-style:italic;font-size:16px;line-height:1.55}
.band-chevron{position:absolute;left:571px;top:134px;width:58px;height:58px;border-radius:50%;background:var(--red);border:4px solid var(--white);display:flex;align-items:center;justify-content:center;z-index:2}

/* models */
.models{top:1370px;height:706px}
.section-title{text-align:center;font-size:21px;font-weight:400}
.section-title b{font-weight:700;text-transform:uppercase}
.section-title b.red{color:var(--red)}
.models .section-title{margin-top:72px}
.model-grid{position:absolute;left:195px;top:148px;display:flex;gap:66px}
.model-card{width:246px;height:516px;border:1px solid var(--line);box-shadow:0 0 8px rgba(0,0,0,.06);text-align:center;padding:20px}
.model-photo{width:206px;height:226px;background:linear-gradient(170deg,#3e5a2a,#d9b21c 45%,#8a3b24 75%,#3e5a2a)}
.model-card h4{font-size:15px;font-weight:500;margin-top:26px}
.model-card .price{color:var(--red-bright);font-weight:600;font-size:15px;margin-top:4px}
.model-card ul{list-style:none;font-size:12px;line-height:24px;margin-top:18px}
.model-card .btn{margin-top:28px;font-size:10px;padding:9px 24px}

/* financing */
.financing{top:2120px;height:480px;background:var(--navy);overflow:hidden}
.financing-photo{position:absolute;right:0;top:0;width:640px;height:480px;background:linear-gradient(160deg,#7aa25e,#9b5a3a 35%,#4f6f92 60%,#3c4a3c);clip-path:polygon(120px 0,100% 0,100% 100%,0 100%)}
.financing-copy{position:absolute;left:195px;top:48px;width:430px;color:var(--white)}
.financing-copy h2{font-weight:400;font-size:22px;text-transform:uppercase;letter-spacing:.5px}
.financing-copy .lead{font-size:14px;line-height:1.7;margin-top:20px}
.financing-copy ul{list-style:none;margin-top:20px;padding-left:14px}
.financing-copy li{display:flex;align-items:center;gap:16px;font-size:12.5px;height:34px}
.dot{width:8px;height:8px;border-radius:50%;background:var(--white);flex:none}

/* reasons */
.reasons{top:2600px;height:413px;background:#f7f7f7}
.reasons .section-title{margin-top:62px}
.reason-icon{position:absolute;top:160px;width:68px;height:68px;border-radius:50%;background:var(--navy);display:flex;align-items:center;justify-content:center}
.reason-col{position:absolute;top:154px;width:360px}
.reason-col h4{font-size:16px;font-weight:500}
.reason-col ul{list-style:none;margin-top:22px}
.reason-col li{font-size:12px;line-height:1.45;display:flex;align-items:center;gap:14px;margin-bottom:16px}
.reason-col .dot{background:var(--navy)}
.reason-col.left{left:120px;text-align:right}
.reason-col.left h4{margin-right:60px}
.reason-col.left li{justify-content:flex-end}
.reason-col.right{left:740px}

/* testimonials */
.testimonials{top:3013px;height:289px;background:var(--white)}
.testimonials .section-title{margin-top:48px}
.quote{position:absolute;top:128px;width:420px;display:flex;gap:26px}
.avatar{width:62px;height:62px;border-radius:50%;background:linear-gradient(160deg,#d8c3b0,#9d8470);flex:none}
.quote p{font-size:11px;line-height:1.65;color:var(--muted)}
.quote .who{font-size:12px;color:var(--ink);margin-top:14px}
.quote.one{left:210px}.quote.two{left:650px}
.quote-divider{position:absolute;left:626px;top:124px;width:1px;height:120px;background:var(--line)}

/* contact */
.contact{top:3302px;height:493px;background:var(--pale)}
.contact-photo{position:absolute;left:180px;top:72px;width:220px;height:320px;background:linear-gradient(170deg,#7aa25e,#8f5a3d 35%,#4f6f92 65%,#3c3c3c)}
.contact-info{position:absolute;left:424px;top:90px;width:250px}
.contact-info h3{font-size:19px;font-weight:600;text-transform:uppercase;line-height:1.35;color:var(--navy)}
.contact-info h3 span{color:var(--red)}
.contact-info .name{font-size:14px;font-weight:600;margin-top:18px}
.contact-info .role{font-size:10px;color:var(--muted)}
.contact-line{display:flex;align-items:center;gap:12px;font-size:12px;margin-top:10px}
.contact-info h5{font-size:14px;font-weight:600;margin-top:24px}
.contact-info address{font-style:normal;font-size:11px;line-height:1.6;margin-top:6px}
.contact-form{position:absolute;left:710px;top:90px;width:330px}
.contact-form h3{font-size:19px;font-weight:500;display:flex;align-items:center;gap:10px}
.contact-form h3::after{content:"";width:34px;height:3px;background:var(--red)}
.field{height:32px;background:var(--white);border:1px solid var(--line);font-size:10px;color:#999;padding:9px 10px;margin-top:10px}
.contact-form .field:first-of-type{margin-top:28px}
.field.msg{height:110px}
.contact-form .btn{margin-top:20px;font-size:10px;padding:10px 26px}

/* map */
.map{top:3795px;height:444px;background:linear-gradient(135deg,#e6e9e3,#d4dccb 40%,#a8c8e0 60%,#e3e6df)}

/* footer */
.site-footer{top:4239px;height:57px;background:var(--navy-dark);color:#c8ccd6;font-size:10px;display:flex;align-items:center;padding:0 180px;justify-content:space-between;text-transform:uppercase}
.social{display:flex;gap:12px}
.social span{width:26px;height:26px;border-radius:50%;background:var(--white)}
</style>
</head>
<body>

<header class="site-header">
  <div class="brand"><span class="brand-mark"></span><span class="brand-name">Tiny Haven Homes</span></div>
  <div class="account-tab">
    <span><svg width="10" height="10" viewBox="0 0 10 10"><rect x="2" y="4" width="6" height="5" fill="#fff"/><path d="M3 4V3a2 2 0 0 1 4 0v1" stroke="#fff" fill="none"/></svg>LOGIN</span>
    <span><svg width="10" height="10" viewBox="0 0 10 10"><circle cx="5" cy="3" r="2" fill="#fff"/><path d="M1 10a4 4 0 0 1 8 0z" fill="#fff"/></svg>REGISTER</span>
  </div>
  <nav class="main-nav">
    <a class="active">Home</a><a>About Tiny</a><a>Tiny Homes</a><a>Models</a><a>Order</a><a>Contact</a>
  </nav>
</header>

<section class="hero" role="img" aria-label="Photo of a red and blue tiny house on a trailer among trees">
  <div class="hero-arrow prev"><svg width="14" height="14" viewBox="0 0 14 14"><path d="M9 2 4 7l5 5" stroke="#333" stroke-width="2.4" fill="none"/></svg></div>
  <div class="hero-arrow next"><svg width="14" height="14" viewBox="0 0 14 14"><path d="m5 2 5 5-5 5" stroke="#333" stroke-width="2.4" fill="none"/></svg></div>
  <div class="hero-inner">
    <h1>Your Dream Home Comes True</h1>
    <p>If you thought that you will never get onto the property ladder let us show you how that can happen and the possibility that you can be financially secure in just a few years from now. Looking at what we have for you might just be the best thing you ever do.</p>
    <span class="btn">Read More</span>
  </div>
</section>

<section class="highlights">
  <div class="offer-card">
    <h2>Stunning House In Your Backyard in The Heart of Your City</h2>
    <div class="sleeps">[SLEEPS UP TO 5 PEOPLE]</div>
    <div class="offer-photo" role="img" aria-label="Photo of a green tiny house in a backyard"></div>
    <div class="note">Enjoy your private space independently</div>
    <div class="price">$ 175 weekly</div>
    <div class="tc">*T&amp;C Apply</div>
    <span class="btn">Buy Now</span>
  </div>
  <div class="likes">
    <h3>What is it that you <b>most</b> Like about a <b>Tiny House?</b></h3>
    <ul>
      <li><span class="plus">+</span>Affordability</li>
      <li><span class="plus">+</span>Compact size</li>
      <li><span class="plus">+</span>Ease of installation</li>
      <li><span class="plus">+</span>Cute appearance</li>
      <li><span class="plus">+</span>Can earn you money</li>
      <li><span class="plus">+</span>Quick to get on your land</li>
      <li><span class="plus">+</span>Extra income</li>
      <li><span class="plus">+</span>Ability to save money and live in it</li>
    </ul>
  </div>
</section>

<section class="question-band">
  <p>Are you seriously thinking of owning a tiny house? What is that you like about a tiny house? How do you see yourself using a Tiny house? Would this be as an investment or for your own use? Or for your own use now, an investment later? Can we make this fit into your budget? Which one is your favorite and what colour?</p>
  <div class="band-chevron"><svg width="20" height="14" viewBox="0 0 20 14"><path d="m3 3 7 7 7-7" stroke="#fff" stroke-width="3" fill="none"/></svg></div>
</section>

<section class="models">
  <h2 class="section-title">All <b>Models</b> Available</h2>
  <div class="model-grid">
    <article class="model-card">
      <div class="model-photo" role="img" aria-label="Photo of a yellow tiny house with red trim"></div>
      <h4>Amber Grove</h4><div class="price">$ 65,000</div>
      <ul><li>3 Bedrooms</li><li>5 people live</li><li>1 lobby</li><li>1 bathroom</li><li>wooded interior</li></ul>
      <span class="btn">Read More</span>
    </article>
    <article class="model-card">
      <div class="model-photo" role="img" aria-label="Photo of a yellow tiny house with red trim"></div>
      <h4>Amber Grove</h4><div class="price">$ 65,000</div>
      <ul><li>3 Bedrooms</li><li>5 people live</li><li>1 lobby</li><li>1 bathroom</li><li>wooded interior</li></ul>
      <span class="btn">Read More</span>
    </article>
    <article class="model-card">
      <div class="model-photo" role="img" aria-label="Photo of a yellow tiny house with red trim"></div>
      <h4>Amber Grove</h4><div class="price">$ 65,000</div>
      <ul><li>2 Bedrooms</li><li>5 people live</li><li>1 lobby</li><li>1 bathroom</li><li>wooded interior</li></ul>
      <span class="btn">Read More</span>
    </article>
  </div>
</section>

<section class="financing">
  <div class="financing-photo" role="img" aria-label="Photo of a red and blue tiny house on a trailer"></div>
  <div class="financing-copy">
    <h2>Financing Your Tiny Home</h2>
    <p class="lead">There are many reasons that YOU may wish to have a TINY HOUSE and at this stage I would ask you :</p>
    <ul>
      <li><span class="dot"></span>Are you seriously thinking of owning a tiny house?</li>
      <li><span class="dot"></span>What is it that you like about a tiny house?</li>
      <li><span class="dot"></span>How do you see yourself using a tiny house?</li>
      <li><span class="dot"></span>Would this be as an investment?</li>
      <li><span class="dot"></span>Or for your own use?</li>
      <li><span class="dot"></span>Or for your own use now, and investment later?</li>
      <li><span class="dot"></span>Can we make this fit into your budget?</li>
      <li><span class="dot"></span>Which one is your favourite and what colour?</li>
    </ul>
  </div>
</section>

<section class="reasons">
  <h2 class="section-title">How do you see yourself using a <b class="red">Tiny House?</b></h2>
  <div class="reason-col left">
    <h4>Many Different Reasons</h4>
    <ul>
      <li>For your own use around the country (travel)<span class="dot"></span></li>
      <li>For you own use in someone's back yard (relative)<span class="dot"></span></li>
      <li>To use yourself now and rent out later to help with<br>your mortgage.<span class="dot"></span></li>
      <li>To rent it out as extra income.<span class="dot"></span></li>
    </ul>
  </div>
  <div class="reason-icon" style="left:528px"><svg width="28" height="34" viewBox="0 0 28 34"><path d="M2 2h16l8 8v22H2z" fill="#fff"/><path d="M7 16h14M7 21h14M7 26h10" stroke="#1f2d50" stroke-width="2"/></svg></div>
  <div class="reason-icon" style="left:648px"><svg width="30" height="30" viewBox="0 0 30 30"><circle cx="15" cy="15" r="13" fill="none" stroke="#fff" stroke-width="2.5"/><text x="15" y="21" text-anchor="middle" fill="#fff" font-family="Montserrat,sans-serif" font-weight="700" font-size="17">$</text></svg></div>
  <div class="reason-col right">
    <h4>Would this be as an Investment?</h4>
    <ul>
      <li><span class="dot"></span>For your own use around the country (travel)</li>
      <li><span class="dot"></span>For you own use in someone's back yard (relative)</li>
      <li><span class="dot"></span>To use yourself now and rent out later to help with<br>your mortgage</li>
      <li><span class="dot"></span>To rent it out as extra income.</li>
    </ul>
  </div>
</section>

<section class="testimonials">
  <h2 class="section-title">What our <b class="red">Clients</b> Thinks?</h2>
  <div class="quote one">
    <div class="avatar" role="img" aria-label="Client portrait"></div>
    <div><p>Leverage agile frameworks to provide a robust synopsis for high level overviews. Iterative approaches to corporate strategy foster collaborative thinking to further the overall value.</p><div class="who">- Corin Ashdale</div></div>
  </div>
  <div class="quote-divider"></div>
  <div class="quote two">
    <div class="avatar" role="img" aria-label="Client portrait"></div>
    <div><p>Leverage agile frameworks to provide a robust synopsis for high level overviews. Iterative approaches to corporate strategy foster collaborative thinking to further the overall value.</p><div class="who">- Corin Ashdale</div></div>
  </div>
</section>

<section class="contact">
  <div class="contact-photo" role="img" aria-label="Photo of a red and blue tiny house"></div>
  <div class="contact-info">
    <h3><span>Tiny Haven</span><br>Homes</h3>
    <div class="name">Aldric Fenmore</div>
    <div class="role">Get in touch with our sales team</div>
    <div class="contact-line"><svg width="12" height="12" viewBox="0 0 12 12"><path d="M2 1h3l1 3-2 1a7 7 0 0 0 3 3l1-2 3 1v3c-6 1-10-3-9-9z" fill="#1f2d50"/></svg>+61-2-5550-1427</div>
    <div class="contact-line"><svg width="12" height="10" viewBox="0 0 12 10"><rect x="0.5" y="0.5" width="11" height="9" fill="none" stroke="#1f2d50"/><path d="m1 1 5 4 5-4" stroke="#1f2d50" fill="none"/></svg>hello@tinyhaven.example</div>
    <div class="contact-line"><svg width="12" height="12" viewBox="0 0 12 12"><rect x="1" y="3" width="10" height="8" fill="#1f2d50"/><rect x="3" y="1" width="6" height="3" fill="#1f2d50"/></svg>+61-2-5550-1428</div>
    <h5>Office Address</h5>
    <address>Level 12, 48 Harbour Lane<br>Sydney 2000 NSW Australia</address>
  </div>
  <form class="contact-form">
    <h3>Drop Us <b>Message</b></h3>
    <div class="field">Your Name</div>
    <div class="field">Your Email Address</div>
    <div class="field">Phone number</div>
    <div class="field msg">Message</div>
    <span class="btn">Submit Now</span>
  </form>
</section>

<section class="map" role="img" aria-label="Street map of the Sydney office location"></section>

<footer class="site-footer">
  <span>© 2018 All rights reserved. Tiny Haven Homes Pty Ltd.</span>
  <div class="social"><span></span><span></span></div>
</footer>

</body>
</html>
```